bottle label/ product label for smoothies (ultra fresh)

Please create a bottle label for our smoothies for retail distribution.
It's important that the following key features are clearly stated:

Ultra-fresh

Handmade

No preservatives

Not heat-treated

No added sugar

The base of the product label should be transparent, so that the color and content of the smoothie can be seen clearly.

We are a young, dynamic company. Our values are honesty, ultra-freshness, and authenticity — and we are the only ones producing this type of product in our country. We are positioned in the premium segment.

Design style: Modern, clean, and natural — but not playful or childish.

Example product: Kelu Kelu (Mango, Pineapple, Lemon, Passion Fruit, Orange)

Wenn du möchtest, kann ich auch gleich einen konkreten Vorschlag für das Etikettendesign auf Englisch oder einen Entwurfstext für das Label selbst erstellen. Sag einfach Bescheid!

Target Market(s)

trade - convenience

Industry/Entity Type

trade

Font styles to use
Sans Serif

Requirements
Must have
• sales- features: Ultra-fresh Handmade No preservatives Not heat-treated No added sugar

```html
<!DOCTYPE html>
<html lang="en">
<head>
<meta charset="utf-8">
<title>Verdalo Smoothie Labels</title>
<link href="https://fonts.googleapis.com/css2?family=Noto+Sans:wght@400;600&display=swap" rel="stylesheet">
<style>
  :root {
    --canvas: #e1e5ea;
    --orange: #df2848;
    --banana: #f6b735;
    --mango: #d8506c;
    --kiwi: #a2b31b;
    --light-ink: #ffffff;
    --dark-ink: #111111;
  }
  html, body {
    margin: 0;
    padding: 0;
    overflow: hidden;
  }
  body {
    width: 1200px;
    height: 560px;
    background: var(--canvas);
    font-family: "Noto Sans", sans-serif;
    position: relative;
  }
  .label {
    position: absolute;
    top: 132px;
    width: 147px;
    height: 390px;
    border-radius: 26px 26px 16px 16px;
    color: var(--light-ink);
  }
  .label--orange { left: 129px; background: var(--orange); }
  .label--banana { left: 315px; background: var(--banana); color: var(--dark-ink); }
  .label--mango  { left: 502px; background: var(--mango); }
  .label--kiwi   { left: 700px; background: var(--kiwi); }

  .brand {
    position: absolute;
    left: 16px;
    top: 92px;
    margin: 0;
    font-size: 20px;
    font-weight: 600;
    line-height: 1;
    letter-spacing: 0.2px;
  }
  .frame {
    position: absolute;
    left: 17px;
    top: 107px;
    width: 106px;
    height: 111px;
    overflow: visible;
  }
  .flavour {
    position: absolute;
    left: 24px;
    top: 135px;
    margin: 0;
    font-size: 17px;
    font-weight: 400;
    line-height: 18px;
    letter-spacing: 0.4px;
    text-transform: uppercase;
  }
  .method {
    position: absolute;
    left: 24px;
    top: 197px;
    margin: 0;
    font-size: 12.5px;
    letter-spacing: 0.3px;
  }
  .features {
    position: absolute;
    left: 0;
    right: 0;
    top: 282px;
    margin: 0;
    padding: 0;
    list-style: none;
    text-align: center;
    font-size: 9.5px;
    line-height: 18.8px;
    letter-spacing: 0.3px;
  }
</style>
</head>
<body>

  <section class="label label--orange">
    <p class="brand">Verdalo</p>
    <svg class="frame" viewBox="0 0 106 111" aria-hidden="true">
      <path d="M1.5 6 V109.5 H104.5 V1.5 H86" fill="none" stroke="currentColor" stroke-width="2.2"/>
    </svg>
    <h2 class="flavour">Orange<br>Smoothie</h2>
    <p class="method">Handmade</p>
    <ul class="features">
      <li>Ultra-fresh</li>
      <li>No preservatives</li>
      <li>Not heat-treated</li>
      <li>No added sugar</li>
    </ul>
  </section>

  <section class="label label--banana">
    <p class="brand">Verdalo</p>
    <svg class="frame" viewBox="0 0 106 111" aria-hidden="true">
      <path d="M1.5 6 V109.5 H104.5 V1.5 H86" fill="none" stroke="currentColor" stroke-width="2.2"/>
    </svg>
    <h2 class="flavour">Banana<br>Smoothie</h2>
    <p class="method">Handmade</p>
    <ul class="features">
      <li>Ultra-fresh</li>
      <li>No preservatives</li>
      <li>Not heat-treated</li>
      <li>No added sugar</li>
    </ul>
  </section>

  <section class="label label--mango">
    <p class="brand">Verdalo</p>
    <svg class="frame" viewBox="0 0 106 111" aria-hidden="true">
      <path d="M1.5 6 V109.5 H104.5 V1.5 H86" fill="none" stroke="currentColor" stroke-width="2.2" style="stroke: var(--dark-ink)"/>
    </svg>
    <h2 class="flavour" style="color: var(--dark-ink)">Mango<br>Smoothie</h2>
    <p class="method" style="color: var(--dark-ink)">Handmade</p>
    <ul class="features" style="color: var(--dark-ink)">
      <li>Ultra-fresh</li>
      <li>No preservatives</li>
      <li>Not heat-treated</li>
      <li>No added sugar</li>
    </ul>
  </section>

  <section class="label label--kiwi">
    <p class="brand">Verdalo</p>
    <svg class="frame" viewBox="0 0 106 111" aria-hidden="true">
      <path d="M1.5 6 V109.5 H104.5 V1.5 H86" fill="none" stroke="currentColor" stroke-width="2.2"/>
    </svg>
    <h2 class="flavour">Kiwi<br>Smoothie</h2>
    <p class="method">Handmade</p>
    <ul class="features">
      <li>Ultra-fresh</li>
      <li>No preservatives</li>
      <li>Not heat-treated</li>
      <li>No added sugar</li>
    </ul>
  </section>

</body>
</html>
```